New Plumbing Company

We are looking for a smart and creative business card design for our new plumbing company. We are looking for creativity and originality in our business cards.

Industry/Entity Type

Plumbing

Contact Information for Business Card

Crestline Plumbing
Peter Halvane
Managing Director
Telephone Number : 0481529604
Email : service@crestlineplumbing.com.au
Website : www.crestlineplumbing.com.au
Lic. 508264K

Colors
0692cd
33a6d7
000000

Requirements
Must have
• I want the business card to be designed on a black background using the blue tones i have selected as seen in the company logo.

```html
<!DOCTYPE html>
<html lang="en">
<head>
<meta charset="utf-8">
<title>Crestline Plumbing – Business Card</title>
<link rel="stylesheet" href="https://fonts.googleapis.com/css2?family=Open+Sans:wght@400;700&display=swap">
<style>
  :root {
    --page-bg: #ffffff;
    --card-bg: #000000;
    --blue-deep: #0692cd;
    --blue-light: #33a6d7;
    --text-white: #ffffff;
    --text-soft: #e6e6e6;
  }
  * { box-sizing: border-box; margin: 0; padding: 0; }
  html, body {
    width: 1200px;
    height: 1000px;
    overflow: hidden;
    background: var(--page-bg);
    font-family: "Open Sans", Arial, sans-serif;
  }
  .sheet {
    width: 1200px;
    height: 1000px;
    display: flex;
    flex-direction: column;
    align-items: center;
    justify-content: center;
    gap: 64px;
  }
  .card {
    position: relative;
    width: 640px;
    height: 392px;
    background: var(--card-bg);
    border-radius: 26px;
    box-shadow: 0 10px 30px rgba(0, 0, 0, 0.25);
    color: var(--text-white);
  }

  /* Front */
  .brand {
    position: absolute;
    top: 92px;
    right: 70px;
    display: flex;
    align-items: center;
    gap: 14px;
  }
  .brand-dot {
    width: 40px;
    height: 40px;
    border-radius: 50%;
    border: 3px solid var(--blue-deep);
  }
  .brand-name {
    font-size: 32px;
    font-weight: 400;
    color: var(--blue-light);
    letter-spacing: 0.5px;
  }
  .contact-block {
    position: absolute;
    left: 64px;
    bottom: 70px;
  }
  .person-name {
    font-size: 19px;
    font-weight: 700;
    color: var(--text-white);
  }
  .person-role {
    font-size: 12px;
    color: var(--text-soft);
    margin-bottom: 22px;
  }
  .contact-list { list-style: none; }
  .contact-item {
    display: flex;
    align-items: center;
    gap: 12px;
    font-size: 13.5px;
    color: var(--text-white);
    margin-top: 8px;
  }
  .contact-icon {
    width: 16px;
    height: 16px;
    flex: none;
  }

  /* Back */
  .back-brand {
    position: absolute;
    inset: 0;
    display: flex;
    align-items: center;
    justify-content: center;
    gap: 18px;
  }
  .back-brand .brand-dot {
    width: 56px;
    height: 56px;
    border-width: 4px;
  }
  .back-brand .brand-name { font-size: 38px; }
</style>
</head>
<body>
<main class="sheet">
  <section class="card card-front" aria-label="Business card front">
    <div class="brand">
      <span class="brand-dot"></span>
      <span class="brand-name">Crestline Plumbing</span>
    </div>
    <div class="contact-block">
      <p class="person-name">Peter Halvane</p>
      <p class="person-role">Managing Director</p>
      <ul class="contact-list">
        <li class="contact-item">
          <svg class="contact-icon" viewBox="0 0 16 16" aria-hidden="true">
            <rect x="4" y="1" width="8" height="14" rx="1.5" fill="none" stroke="#0692cd" stroke-width="1.4"/>
            <line x1="7" y1="12.5" x2="9" y2="12.5" stroke="#0692cd" stroke-width="1.4"/>
          </svg>
          <span>0481529604</span>
        </li>
        <li class="contact-item">
          <svg class="contact-icon" viewBox="0 0 16 16" aria-hidden="true">
            <circle cx="8" cy="8" r="6.5" fill="none" stroke="#0692cd" stroke-width="1.3"/>
            <ellipse cx="8" cy="8" rx="2.8" ry="6.5" fill="none" stroke="#0692cd" stroke-width="1.1"/>
            <line x1="1.5" y1="8" x2="14.5" y2="8" stroke="#0692cd" stroke-width="1.1"/>
          </svg>
          <span>www.crestlineplumbing.com.au</span>
        </li>
        <li class="contact-item">
          <svg class="contact-icon" viewBox="0 0 16 16" aria-hidden="true">
            <rect x="1" y="3" width="14" height="10" fill="#0692cd"/>
            <polyline points="1,3 8,9 15,3" fill="none" stroke="#000" stroke-width="1.2"/>
          </svg>
          <span>service@crestlineplumbing.com.au</span>
        </li>
      </ul>
    </div>
  </section>

  <section class="card card-back" aria-label="Business card back">
    <div class="back-brand">
      <span class="brand-dot"></span>
      <span class="brand-name">Crestline Plumbing</span>
    </div>
  </section>
</main>
</body>
</html>
```